Business card for law firm

Need business card for new law firm. Think confident, authoritative, conservative, but not stuffy or old-fashioned.

Contact Information for Business Card

Content for card - logo (uploaded), plus the following:

Paul Wexbury (larger font)
Managing Partner (larger font, but not as large as name)
Level 9, 41 Tansy Lane
Sydney NSW 2000
Main Tel 02 7346 2190
Direct Tel 02 6273 4415
Email paul@qvlegal.com.au
www.qvlegal.com.au

Letterhead design should include logo plus:
Level 9, 41 Tansy Lane
Sydney NSW 2000
Tel 02 6273 4415
www.qvlegal.com.au

```html
<!DOCTYPE html>
<html lang="en">
<head>
<meta charset="utf-8">
<title>QV Legal — Business Card</title>
<link rel="stylesheet" href="https://fonts.googleapis.com/css2?family=Cinzel:wght@400&family=Open+Sans:wght@400&display=swap">
<style>
  :root {
    --backdrop: #262626;
    --navy: #1c2257;
    --paper: #ffffff;
    --ink: #1f1f2a;
    --rule: #6b6b6b;
  }
  * { margin: 0; padding: 0; box-sizing: border-box; }
  html, body {
    width: 1200px; height: 858px; overflow: hidden;
    background: var(--backdrop);
  }
  .canvas { position: relative; width: 1200px; height: 858px; }

  .card {
    position: absolute;
    width: 560px; height: 320px;
    border-radius: 22px;
    overflow: hidden;
  }

  /* Back of card */
  .card-back {
    left: 30px; top: 110px;
    background: var(--navy);
  }
  .card-back .brand {
    position: absolute; right: 48px; bottom: 110px;
    display: flex; flex-direction: column; align-items: center; gap: 10px;
  }
  .card-back .brand-mark {
    width: 40px; height: 40px; background: var(--paper);
  }
  .card-back .brand-name {
    font-family: "Cinzel", serif; font-weight: 400;
    font-size: 38px; letter-spacing: 1px; color: var(--paper); line-height: 1;
  }

  /* Front of card */
  .card-front {
    left: 610px; top: 418px;
    background: var(--paper);
  }
  .card-front .brand {
    position: absolute; left: 20px; top: 112px; width: 220px;
    display: flex; flex-direction: column; align-items: center; gap: 10px;
  }
  .card-front .brand-mark {
    width: 36px; height: 36px; background: var(--navy);
  }
  .card-front .brand-name {
    font-family: "Cinzel", serif; font-weight: 400;
    font-size: 32px; letter-spacing: 1px; color: var(--ink); line-height: 1;
    white-space: nowrap;
  }
  .divider {
    position: absolute; left: 262px; top: 66px;
    width: 1px; height: 190px; background: var(--rule);
  }
  .details {
    position: absolute; left: 290px; top: 68px;
    font-family: "Open Sans", sans-serif; color: var(--ink);
  }
  .person-name {
    font-family: "Cinzel", serif; font-weight: 400; font-size: 24px;
    color: var(--navy); line-height: 1; letter-spacing: 0.5px;
  }
  .person-role { font-size: 14px; margin-top: 5px; }
  .address { font-size: 12.5px; line-height: 1.35; margin-top: 12px; }
  .contact { list-style: none; margin-top: 8px; font-size: 12.5px; line-height: 1.5; }
  .contact li { display: flex; align-items: center; gap: 8px; white-space: nowrap; }
  .contact svg { width: 10px; height: 10px; fill: var(--navy); flex: none; }
  .contact .label { display: inline-block; width: 66px; }
</style>
</head>
<body>
<main class="canvas">

  <section class="card card-back" aria-label="Card back">
    <div class="brand">
      <span class="brand-mark"></span>
      <span class="brand-name">QV Legal</span>
    </div>
  </section>

  <section class="card card-front" aria-label="Card front">
    <div class="brand">
      <span class="brand-mark"></span>
      <span class="brand-name">QV Legal</span>
    </div>

    <div class="divider"></div>

    <div class="details">
      <h1 class="person-name">Paul Wexbury</h1>
      <p class="person-role">Managing Partner</p>
      <p class="address">Level 9, 41 Tansy Lane<br>Sydney NSW 2000</p>
      <ul class="contact">
        <li>
          <svg viewBox="0 0 10 10" aria-hidden="true"><path d="M2 0.5 L3.6 2.6 L2.8 3.6 C3.4 5 4.8 6.4 6.4 7.2 L7.4 6.4 L9.5 8 L8.4 9.5 C4.6 9.2 0.8 5.4 0.5 1.6 Z"/></svg>
          <span><span class="label">Main Tel</span>02 7346 2190</span>
        </li>
        <li>
          <svg viewBox="0 0 10 10" aria-hidden="true"><path d="M2 0.5 L3.6 2.6 L2.8 3.6 C3.4 5 4.8 6.4 6.4 7.2 L7.4 6.4 L9.5 8 L8.4 9.5 C4.6 9.2 0.8 5.4 0.5 1.6 Z"/></svg>
          <span><span class="label">Direct Tel</span>02 6273 4415</span>
        </li>
        <li>
          <svg viewBox="0 0 10 10" aria-hidden="true"><path d="M0.5 2 H9.5 V8.5 H0.5 Z M0.5 2 L5 5.6 L9.5 2" stroke="#fff" stroke-width="0.8"/></svg>
          paul@qvlegal.com.au
        </li>
        <li>
          <svg viewBox="0 0 10 10" aria-hidden="true"><circle cx="5" cy="5" r="4.5"/><path d="M0.5 5 H9.5 M5 0.5 C2.6 3 2.6 7 5 9.5 M5 0.5 C7.4 3 7.4 7 5 9.5" stroke="#fff" stroke-width="0.6" fill="none"/></svg>
          www.qvlegal.com.au
        </li>
      </ul>
    </div>
  </section>

</main>
</body>
</html>
```